Business brochure for a human resources company

I am looking for a commercial brochure for my company which is based on payroll management and human resources.
I wish it had the same colors and design as the logo, Gold and Black.
I would like to highlight the services of my company.
The brochure should show the quality, professionalism and modernity of the company.
The company has two poles, a legal and a social
A place must show the company logo
The target audience is accounting firms as well as small and medium enterprises.
Small and Medium Enterprise, Accounting firm
Paie et Ressources humaines

```html
<!DOCTYPE html>
<html lang="fr">
<head>
<meta charset="utf-8">
<title>VALORIS – Conseil et Gestion</title>
<link href="https://fonts.googleapis.com/css2?family=Montserrat:wght@300;400;500;700;800&family=Poppins:ital,wght@1,800&family=Roboto:wght@400;700&display=swap" rel="stylesheet">
<style>
  :root{
    --page:#ececec;
    --black:#000;
    --white:#fff;
    --grey:#dcdcdc;
    --gold:#c9a24a;
    --gold-light:#f0d57a;
    --gold-dark:#8a6520;
    --photo-blue-1:#bff2ff;
    --photo-blue-2:#1a9fd0;
    --photo-blue-3:#06304f;
    --photo-warm-1:#e9c9a0;
    --photo-warm-2:#8a6d55;
    --photo-warm-3:#2d2a2a;
  }
  *{margin:0;padding:0;box-sizing:border-box}
  html,body{width:789px;height:1200px;overflow:hidden;background:var(--page)}
  body{position:relative;font-family:"Montserrat",sans-serif;color:var(--white)}

  .panel{position:absolute;left:55px;width:682px;height:527px;background:var(--black);overflow:hidden}
  .panel--cover{top:69px}
  .panel--inside{top:615px}
  .abs{position:absolute}
  .deco{position:absolute;left:0;top:0;width:682px;height:527px}

  /* brand */
  .brand{position:absolute;text-align:center;transform:translateX(-50%)}
  .brand__name{font-family:"Montserrat",sans-serif;font-weight:700;color:var(--gold);letter-spacing:1px;line-height:1}
  .brand__tag{font-weight:500;letter-spacing:2.6px;color:var(--white);line-height:1;margin-top:4px}
  .brand__dot{display:block;margin:0 auto 6px;border-radius:50%;background:var(--gold)}
  .brand--main{left:512px;top:28px}
  .brand--main .brand__dot{width:44px;height:44px}
  .brand--main .brand__name{font-size:32px}
  .brand--main .brand__tag{font-size:8px}
  .brand--footer{left:92px;top:424px}
  .brand--footer .brand__dot{width:30px;height:30px}
  .brand--footer .brand__name{font-size:21px}
  .brand--footer .brand__tag{font-size:6px;letter-spacing:2.2px}

  /* photo placeholders */
  .photo{position:absolute;border-radius:50%}
  .photo--hr{left:396px;top:136px;width:226px;height:226px;
    background:radial-gradient(circle at 45% 45%,var(--photo-blue-1) 0%,var(--photo-blue-2) 45%,var(--photo-blue-3) 100%)}
  .photo--handshake{left:400px;top:-77px;width:310px;height:310px;
    background:radial-gradient(circle at 45% 55%,var(--photo-warm-1) 0%,var(--photo-warm-2) 45%,var(--photo-warm-3) 100%)}
  .photo--charts{left:0;top:330px;width:280px;height:280px;
    background:radial-gradient(circle at 55% 40%,#f2f0ee 0%,#cfc7c0 40%,#5b5550 100%)}

  /* cover */
  .headline{position:absolute;left:509px;top:416px;transform:translateX(-50%);text-align:center;
    font-family:"Poppins",sans-serif;font-style:italic;font-weight:800;white-space:nowrap;line-height:1}
  .headline__lead{font-size:25px;display:block;margin-bottom:8px}
  .headline__rest{font-size:15.5px;display:block;line-height:24px}

  .about{position:absolute;left:48px;top:143px;width:244px;height:189px;border:1.2px solid var(--gold);border-radius:14px;
    outline:1px solid var(--gold-dark);outline-offset:-4px;text-align:center;font-family:"Roboto",sans-serif}
  .about__title{font-family:"Montserrat",sans-serif;font-weight:800;font-size:11.5px;margin-top:16px;letter-spacing:.3px}
  .about__text{font-size:7.2px;line-height:9.3px;margin:8px 16px 0}
  .about__text + .about__text{margin-top:3px}
  .about__name{font-family:"Montserrat",sans-serif;font-weight:700;color:var(--gold);font-size:15px;margin-top:9px;letter-spacing:.5px}
  .about__sub{font-size:8px;margin-top:4px}

  .contact{position:absolute;left:175px;top:386px;font-family:"Roboto",sans-serif;font-size:7.4px;line-height:11px}
  .contact__row{display:flex;align-items:flex-start;margin-bottom:7px}
  .contact__row--tight{margin-bottom:0}
  .contact__icon{width:12px;height:11px;margin-right:10px;flex:none;display:flex;align-items:center;justify-content:center}
  .contact__icon svg{width:10px;height:10px}

  /* inside */
  .pole-title{position:absolute;font-weight:800;font-size:16.5px;color:var(--grey);letter-spacing:.3px}
  .pole-title--social{left:44px;top:45px}
  .pole-title--legal{left:382px;top:291px}

  .service{position:absolute}
  .service__icon{position:absolute;width:22px;height:22px}
  .service__name{font-weight:300;color:var(--gold);font-size:11px;letter-spacing:.2px;line-height:10px;white-space:nowrap}
  .service__list{list-style:none;margin-top:6px}
  .service__list li{position:relative;padding-left:16px;font-size:8.4px;line-height:11.2px;letter-spacing:.25px;white-space:nowrap}
  .service__list li::before{content:"";position:absolute;left:1px;top:2.5px;width:6px;height:6px;border:.8px solid var(--white);border-radius:50%}
  .service__list li::after{content:"";position:absolute;left:3.2px;top:4px;width:2px;height:3px;border:solid var(--white);border-width:0 .8px .8px 0;transform:rotate(40deg)}
  .service__list--bold li{font-weight:500}

  .social .service__name{padding-left:0}
  .s-pay{left:73px;top:80px}
  .s-admin{left:73px;top:147px}
  .s-bdese{left:75px;top:250px}
  .s-bdese .service__name{line-height:9.5px;white-space:normal;width:230px}
  .s-bdese .service__list{margin-top:5px}
  .social .service__list{margin-left:2px}
  .social .service__list li{padding-left:17px}

  .legal .service__list li{font-size:8.2px;padding-left:11px}
  .legal .service__list li::before{left:0;width:5.5px;height:5.5px}
  .legal .service__list li::after{left:2px;top:3.8px}
  .l-create{left:416px;top:329px}
  .l-admin{left:416px;top:386px}
  .l-quali{left:416px;top:416px}
  .l-create .service__list,.l-quali .service__list{margin-left:4px;margin-top:5px}
</style>
</head>
<body>

<!-- Cover spread -->
<section class="panel panel--cover">
  <svg class="deco" viewBox="0 0 682 527" aria-hidden="true">
    <defs>
      <linearGradient id="goldCover" x1="0" y1="0" x2="1" y2="1">
        <stop offset="0" stop-color="#8a6520"/>
        <stop offset=".45" stop-color="#f0d57a"/>
        <stop offset="1" stop-color="#a57b2c"/>
      </linearGradient>
    </defs>
    <circle cx="512" cy="256" r="129" fill="url(#goldCover)"/>
    <circle cx="515" cy="249" r="121" fill="#000"/>
  </svg>
  <div class="photo photo--hr" role="img" aria-label="Photo : main touchant une interface numérique bleue de ressources humaines"></div>

  <div class="brand brand--main">
    <span class="brand__dot"></span>
    <div class="brand__name">VALORIS</div>
    <div class="brand__tag">CONSEIL ET GESTION</div>
  </div>

  <h1 class="headline">
    <span class="headline__lead">POURQUOI FAIRE</span>
    <span class="headline__rest">COMPLIQUÉ QUAND ON PEUT</span>
    <span class="headline__rest">FAIRE VALORIS ?</span>
  </h1>

  <div class="about">
    <h2 class="about__title">ABOUT US</h2>
    <p class="about__text">VALORIS Conseil et gestion a été pensée et conçue dans le but de simplifier la gestion sociale et juridique des cabinets d’expertise comptable, en créant des solutions sur-mesure adaptées à votre stratégie et votre budget, avec le niveau d’externalisation qui correspond à vos besoins. Avec VALORIS Conseil et Gestion vous gagnerez du temps, vous réduirez vos coûts, et vous vous concentrerez sur votre cœur de métier.</p>
    <p class="about__text">L’équipe VALORIS est à votre disposition pour<br>toute demande d’information.</p>
    <div class="about__name">VALORIS</div>
    <div class="about__sub">Conseil et Gestion</div>
  </div>

  <div class="brand brand--footer">
    <span class="brand__dot"></span>
    <div class="brand__name">VALORIS</div>
    <div class="brand__tag">CONSEIL ET GESTION</div>
  </div>

  <address class="contact" style="font-style:normal">
    <div class="contact__row">
      <span class="contact__icon"><svg viewBox="0 0 10 10"><path d="M5 0.5a3.3 3.3 0 0 0-3.3 3.3C1.7 6.3 5 9.7 5 9.7s3.3-3.4 3.3-5.9A3.3 3.3 0 0 0 5 .5zm0 4.6a1.3 1.3 0 1 1 0-2.6 1.3 1.3 0 0 1 0 2.6z" fill="var(--gold)"/></svg></span>
      <span>Siège social : 12 Rue des Tilleuls<br>– 95000 Cergy</span>
    </div>
    <div class="contact__row">
      <span class="contact__icon"><svg viewBox="0 0 10 10"><path d="M2.2.6l1.5 2-.8 1.1c.6 1.3 1.6 2.3 2.9 2.9l1.1-.8 2 1.5-.8 1.9C4.6 9.2.8 5.4.3 1.4z" fill="var(--gold)"/></svg></span>
      <span>N°Tél: 07.00.00.12.34</span>
    </div>
    <div class="contact__row contact__row--tight">
      <span class="contact__icon"><svg viewBox="0 0 10 10"><rect x="1" y="3" width="8" height="5.5" rx="1" fill="var(--gold)"/><rect x="2.5" y="1" width="5" height="2" rx=".8" fill="var(--gold)"/></svg></span>
      <span>N°Siret : 000 123 456 00010</span>
    </div>
    <div class="contact__row contact__row--tight">
      <span class="contact__icon"><svg viewBox="0 0 10 10"><rect x="1" y="1.5" width="7" height="7.5" rx="1" fill="none" stroke="var(--gold)" stroke-width="1.1"/><path d="M4 6l.3-1.3L8.3.8l1 1-4 4z" fill="var(--gold)"/></svg></span>
      <span>Code NAF : 8299Z</span>
    </div>
    <div class="contact__row contact__row--tight">
      <span class="contact__icon"><svg viewBox="0 0 10 10"><rect x="1" y="1" width="8" height="8" fill="none" stroke="var(--gold)" stroke-width="1"/><rect x="3" y="3" width="4" height="4" fill="var(--gold)"/></svg></span>
      <span>Enregistré au RCS de Cergy</span>
    </div>
    <div class="contact__row">
      <span class="contact__icon"></span>
      <span>N° SIREN 000 123 456</span>
    </div>
    <div class="contact__row">
      <span class="contact__icon"><svg viewBox="0 0 10 10"><rect x=".6" y="2" width="8.8" height="6" fill="none" stroke="var(--gold)" stroke-width=".9"/><path d="M.6 2L5 5.6 9.4 2" fill="none" stroke="var(--gold)" stroke-width=".9"/></svg></span>
      <span>contact@valoris-gestion.fr</span>
    </div>
  </address>
</section>

<!-- Inside spread -->
<section class="panel panel--inside">
  <svg class="deco" viewBox="0 0 682 527" aria-hidden="true">
    <defs>
      <linearGradient id="goldInside" x1="0" y1="0" x2="1" y2="1">
        <stop offset="0" stop-color="#8a6520"/>
        <stop offset=".5" stop-color="#f0d57a"/>
        <stop offset="1" stop-color="#a57b2c"/>
      </linearGradient>
      <linearGradient id="goldLine" x1="0" y1="0" x2="1" y2="0">
        <stop offset="0" stop-color="#8a6520"/>
        <stop offset=".5" stop-color="#f0d57a"/>
        <stop offset="1" stop-color="#a57b2c"/>
      </linearGradient>
    </defs>
    <circle cx="543" cy="87" r="168" fill="url(#goldInside)"/>
    <circle cx="155" cy="462" r="148" fill="url(#goldInside)"/>
    <!-- frame lines, social -->
    <path d="M24 25H81M38 29H172" stroke="url(#goldLine)" stroke-width="1.2" fill="none"/>
    <path d="M24 25V90M28 30V188" stroke="var(--gold)" stroke-width="1.2" fill="none"/>
    <!-- frame lines, legal -->
    <path d="M653 337V486M657 446V502" stroke="var(--gold)" stroke-width="1.2" fill="none"/>
    <path d="M509 497H643M517 501H657" stroke="url(#goldLine)" stroke-width="1.2" fill="none"/>
  </svg>
  <div class="photo photo--handshake" role="img" aria-label="Photo : poignée de main d’affaires devant une ville, icônes de réseau"></div>
  <div class="photo photo--charts" role="img" aria-label="Photo : mains analysant des graphiques sur un document, ordinateur portable"></div>

  <div class="social">
    <h2 class="pole-title pole-title--social">PÔLE SOCIAL :</h2>

    <svg class="service__icon" style="left:43px;top:79px" viewBox="0 0 22 22" aria-hidden="true">
      <circle cx="9" cy="7" r="4" fill="var(--gold)"/><path d="M1 20c0-5 3.5-7.5 8-7.5s8 2.5 8 7.5z" fill="var(--gold)"/><circle cx="17.5" cy="14.5" r="3" fill="none" stroke="var(--gold)" stroke-width="1.6"/>
    </svg>
    <div class="service s-pay">
      <h3 class="service__name">Processus de paie :</h3>
      <ul class="service__list">
        <li>Recherche des variables</li>
        <li>Établissement des fiches de paie</li>
        <li>DSN</li>
        <li>Audit des fiches de paie</li>
      </ul>
    </div>

    <svg class="service__icon" style="left:43px;top:146px" viewBox="0 0 22 22" aria-hidden="true">
      <path d="M4 8a8 8 0 0 1 13-4M18 14a8 8 0 0 1-13 4" fill="none" stroke="var(--gold)" stroke-width="1.4"/><rect x="8" y="9" width="6" height="6" fill="var(--gold)"/><circle cx="19" cy="4" r="2" fill="var(--gold)"/><circle cx="3" cy="18" r="2" fill="var(--gold)"/>
    </svg>
    <div class="service s-admin">
      <h3 class="service__name">Administration du personnel :</h3>
      <ul class="service__list">
        <li>Gestion des procédures et documents en droits<br>du travail</li>
        <li>Gestion des absences</li>
        <li>Gestion du temps</li>
        <li>Étude et analyse (absentéisme, maladie...)</li>
        <li>Conseil et aide pour améliorer les performances<br>de l’entreprise sous l’angle RH</li>
      </ul>
    </div>

    <svg class="service__icon" style="left:43px;top:249px" viewBox="0 0 22 22" aria-hidden="true">
      <ellipse cx="11" cy="4" rx="8" ry="2.6" fill="var(--gold)"/><path d="M3 6.5c0 1.5 3.6 2.6 8 2.6s8-1.1 8-2.6V9c0 1.5-3.6 2.6-8 2.6S3 10.5 3 9zM3 11.5c0 1.5 3.6 2.6 8 2.6s8-1.1 8-2.6V14c0 1.5-3.6 2.6-8 2.6S3 15.5 3 14zM3 16.5c0 1.5 3.6 2.6 8 2.6s8-1.1 8-2.6V19c0 1.5-3.6 2.6-8 2.6S3 20.5 3 19z" fill="var(--gold)"/>
    </svg>
    <div class="service s-bdese">
      <h3 class="service__name">Base de Données Économique, Sociale et Environnementale (BDESE)</h3>
      <ul class="service__list service__list--bold">
        <li>Création</li>
        <li>Suivi et mise a jour</li>
      </ul>
    </div>
  </div>

  <div class="legal">
    <h2 class="pole-title pole-title--legal">PÔLE JURIDIQUE :</h2>

    <svg class="service__icon" style="left:381px;top:330px;width:24px;height:24px" viewBox="0 0 22 22" aria-hidden="true">
      <path d="M3 3l3 3-1.3 2c1.2 2.6 3 4.4 5.6 5.6l2-1.3 3 3-1.6 3.2C7.5 18 2.5 13 .8 6z" fill="var(--gold)"/><rect x="12" y="1" width="8" height="7" fill="var(--gold)"/>
    </svg>
    <div class="service l-create">
      <h3 class="service__name">Conseil et aide à la création d’entreprise</h3>
      <ul class="service__list">
        <li>Conseil et aide à la création d’entreprise</li>
        <li>Écriture des statuts</li>
      </ul>
    </div>

    <svg class="service__icon" style="left:384px;top:380px" viewBox="0 0 22 22" aria-hidden="true">
      <circle cx="11" cy="6" r="4.5" fill="var(--gold)"/><path d="M2 20c0-5 4-7.5 9-7.5s9 2.5 9 7.5z" fill="var(--gold)"/>
    </svg>
    <div class="service l-admin">
      <h3 class="service__name">Externalisation de la partie administrative</h3>
    </div>

    <svg class="service__icon" style="left:384px;top:418px" viewBox="0 0 22 22" aria-hidden="true">
      <path d="M4 1h10l5 5v15H4z" fill="var(--gold)"/><path d="M7 9h9M7 12.5h9M7 16h6" stroke="#000" stroke-width="1.2"/>
    </svg>
    <div class="service l-quali">
      <h3 class="service__name">Dossier Qualivéa</h3>
      <ul class="service__list">
        <li>Aide à la création du dossier Qualivéa</li>
        <li>Représentation devant le jury Qualivéa</li>
      </ul>
    </div>
  </div>
</section>

</body>
</html>
```